Walking in Grace book cover

Needing a book cover design and I have attached 3 sample covers for a starting point. I would like the design to use similar font as the sample cover along with a red and white theme. I would like a background image of broken shackles. On the back cover leave room for the author's bio and picture. The front cover and book details are below:
Book size: 6x9 or. 4.5x7
Title: Walking in Grace
Subtitle: Standing Firm Against Every Snare Through Scripture
Author: Marlon Petway
No spine is needed for the book due to it is a smaller book and the text will not fit. Yes, we are looking at every design and will choose winner on or before 4/20/2022

```html
<!DOCTYPE html>
<html lang="en">
<head>
<meta charset="utf-8">
<title>Walking in Grace — Book Cover</title>
<link rel="stylesheet" href="https://fonts.googleapis.com/css2?family=Crimson+Pro:wght@400;500&display=swap">
<style>
  :root {
    --backdrop: #8a8a8a;
    --paper: #ffffff;
    --title-red: #e22c2f;
    --frame-gold: #f6d20a;
    --ink: #111111;
    --edge-crimson: #b01535;
    --art-light: #f1f1f1;
    --art-mid: #c9c9c9;
  }
  * { margin: 0; padding: 0; box-sizing: border-box; }
  html, body {
    width: 1200px;
    height: 1200px;
    overflow: hidden;
    background: var(--backdrop);
  }
  .book-cover {
    position: absolute;
    left: 238px;
    top: 56px;
    width: 724px;
    height: 1088px;
    background: var(--paper);
    border-top: 2px solid var(--edge-crimson);
    font-family: "Crimson Pro", "Times New Roman", serif;
    color: var(--ink);
  }
  .cover-art {
    position: absolute;
    left: 42px;
    top: 34px;
    width: 640px;
    height: 274px;
    background: radial-gradient(ellipse at center, var(--art-light) 0%, var(--art-mid) 100%);
  }
  .title-panel {
    position: absolute;
    left: 43px;
    top: 306px;
    width: 640px;
    height: 384px;
    background: var(--title-red);
    border: 3px solid var(--frame-gold);
  }
  .title-panel svg {
    display: block;
    width: 100%;
    height: 100%;
  }
  .title-word {
    fill: var(--paper);
    font-family: "Crimson Pro", "Times New Roman", serif;
    font-weight: 500;
  }
  .title-rule {
    stroke: var(--paper);
    stroke-width: 1.5;
  }
  .subtitle {
    position: absolute;
    left: 0;
    top: 712px;
    width: 100%;
    text-align: center;
    font-size: 41px;
    font-weight: 500;
    line-height: 1.05;
  }
  .divider {
    position: absolute;
    left: 117px;
    top: 899px;
    width: 509px;
    height: 3px;
    background: linear-gradient(90deg, transparent 0%, var(--ink) 12%, var(--ink) 88%, transparent 100%);
    border-radius: 50%;
  }
  .author-name {
    position: absolute;
    left: 0;
    top: 920px;
    width: 100%;
    text-align: center;
    font-size: 84px;
    font-weight: 500;
    line-height: 1;
  }
</style>
</head>
<body>
  <main class="book-cover">
    <div class="cover-art" role="img" aria-label="Engraved illustration of two raised fists breaking free from shackles, chain links scattering between them"></div>

    <div class="title-panel">
      <svg viewBox="0 0 634 378" aria-label="Walking in Grace">
        <text class="title-word" x="317" y="145" font-size="142" text-anchor="middle" textLength="570" lengthAdjust="spacingAndGlyphs">WALKING</text>
        <line class="title-rule" x1="44" y1="192" x2="250" y2="192"/>
        <line class="title-rule" x1="384" y1="192" x2="590" y2="192"/>
        <text class="title-word" x="317" y="218" font-size="68" text-anchor="middle">IN</text>
        <text class="title-word" x="317" y="350" font-size="150" text-anchor="middle" textLength="500" lengthAdjust="spacingAndGlyphs">GRACE</text>
      </svg>
    </div>

    <p class="subtitle">Standing Firm Against Every Snare<br>Through Scripture</p>

    <div class="divider"></div>

    <p class="author-name">Marlon Petway</p>
  </main>
</body>
</html>
```